Flyer für gemeinnützige Organisation designen
5 von 5 Sternen, und wir würden noch mehr geben, wenn e smöglich wäre. Obwohl wir für die endgültigen Änderungen mehr Zeit als geplant brauchten, war der Designer sehr freundlich, zuvorkommend und geduldig mit uns. Er hat alle unsere Wünsche schnell und zu unserer vollsten Zufriedenheit umgesetzt und für uns wunderschöne Flyer gestaltet. Wir sind sehr glücklich über das tolle Design und können jedem den Designer weiterempfehlen. Ganz lieben Dank nochmal! :-)
Zielgruppe
Der Name VELTORIS setzt sich zusammen aus 'Human' - der Mensch, 'Umma' - die Gemeinschaft und 'Aid' - die Hilfe. Die Gemeinschaft aller Menschen, unabhängig von Herkunft und Religion ist der gemeinsame Nenner, dem wir uns verschrieben haben.
Unsere Vision ist es Waisenkindern ein neues Zuhause zu schaffen wo Sie sicher und behütet aufwachsen können. Wir möchten Kindern, die in ihren jungen Jahren schon unglaubliches Leid erleben mussten die Chance auf eine echte Kindheit mit glücklichen Erinnerungen zurückgeben.
VELTORIS ist Persönlich. Transparent. Authentisch. Einfach anders.
Unsere Zielgruppe ist jeder der helfen kann und möchte, dabei spielt das 'wie' keine Rolle.
Aufgabenstellung
Neben vielen anderen Projekten, soll das Waisenhaus und ggf. eine Patenschaft für ein Kind im Vorderung stehen.
Die Flyer werden für eine Charity Action benötigt und zum auslegen.
Bevorzugt hätten wir gerne Flyer zum aufklappen. Alle weiteren Informationen (Kontaktdaten/Spendenoptionen etc. ) finden Sie auf www.veltoris.org
Sie können auch gerne Fotos von der Homepage oder unserem Instagram-Account verwenden.
Im weiteren Verlauf benötigen wir auch Plakete für ein Charity Event (Golf-Cub) am 14.05.2022 im Golfclub Wendra14, Falkenrainweg 38, 47506 Neukirchen-Vluyn.

```html
<!DOCTYPE html>
<html lang="de">
<head>
<meta charset="utf-8">
<title>VELTORIS Flyer</title>
<link rel="stylesheet" href="https://fonts.googleapis.com/css2?family=Roboto:wght@400;700&display=swap">
<style>
  :root {
    --green: #3f9f36;
    --text: #4d4d4d;
    --white: #ffffff;
    --page: #ffffff;
    --shadow: rgba(0,0,0,0.3);
    --photo-top: #8c7f58;
    --photo-trees: #7d8050;
    --photo-banner: #ebe2e6;
    --photo-banner-edge: #d9ccd2;
    --photo-sand: #b48d66;
    --photo-ground: #a2744f;
  }
  * { box-sizing: border-box; margin: 0; padding: 0; }
  html, body { width: 1200px; height: 2400px; overflow: hidden; background: var(--page); }
  body { position: relative; font-family: 'Roboto', Arial, sans-serif; color: var(--text); }

  .card {
    position: absolute;
    left: 135px;
    width: 928px;
    box-shadow: 0 6px 18px var(--shadow);
    overflow: hidden;
  }
  .card--front { top: 500px; height: 658px; }
  .card--back { top: 1238px; height: 660px; background: var(--white); }

  .front-photo {
    width: 100%; height: 100%;
    background: linear-gradient(180deg,
      var(--photo-top) 0%,
      var(--photo-trees) 12%,
      var(--photo-banner-edge) 20%,
      var(--photo-banner) 32%,
      var(--photo-banner) 62%,
      var(--photo-banner-edge) 72%,
      var(--photo-sand) 84%,
      var(--photo-ground) 100%);
  }

  .back-info { position: relative; height: 463px; }
  .heading {
    position: absolute;
    left: 63px;
    color: var(--green);
    font-weight: 700;
    font-size: 38px;
    line-height: 44px;
  }
  .heading--why { top: 26px; }
  .heading--donate { top: 314px; }
  .body-text {
    position: absolute;
    font-weight: 400;
    font-size: 17.3px;
    line-height: 21.2px;
    white-space: nowrap;
  }
  .column-left { left: 63px; top: 76px; }
  .column-right { left: 480px; top: 76px; }
  .column-left p + p { margin-top: 21.2px; }
  .donate-note { left: 63px; top: 381px; }

  .donate-band {
    position: absolute; left: 0; right: 0; bottom: 0;
    height: 197px;
    background: var(--green);
    color: var(--white);
  }
  .brand {
    position: absolute; left: 0; top: 0; width: 299px; height: 100%;
    display: flex; flex-direction: column; align-items: center; justify-content: center; gap: 14px;
  }
  .brand-dot { width: 50px; height: 50px; border-radius: 50%; background: var(--white); }
  .brand-name { font-weight: 400; font-size: 20px; letter-spacing: 7px; }
  .divider { position: absolute; left: 299px; top: 26px; width: 2px; height: 144px; background: var(--white); }
  .donate-options {
    position: absolute; left: 332px; top: 26px;
    display: grid;
    grid-template-columns: 180px 180px 180px;
    text-align: center;
    font-weight: 400;
    font-size: 17.3px;
    line-height: 21px;
  }
  .option { display: flex; flex-direction: column; align-items: center; }
  .option-icon { width: 44px; height: 44px; margin-bottom: 36px; }
  .option-mark { width: 38px; height: 38px; border-radius: 50%; background: var(--white); margin: 3px 0 39px; }
</style>
</head>
<body>
  <section class="card card--front">
    <div class="front-photo" role="img" aria-label="Foto: vier Kinder vor einem hellen Banner der Organisation in Burkina Faso, ein Junge hält ein Puzzlespiel, im Hintergrund Bäume und Gebäude, sandiger Boden"></div>
  </section>

  <section class="card card--back">
    <div class="back-info">
      <h2 class="heading heading--why">Warum VELTORIS?</h2>
      <div class="body-text column-left">
        <p>Der Name VELTORIS setzt sich zusammen aus<br>„Human“ - der Mensch, „Umma“ - die Gemein-<br>schaft und „Aid“ - die Hilfe. Die Gemeinschaft<br>aller Menschen, unabhängig von Herkunft und<br>Religion ist der gemeinsame Nenner, dem wir<br>uns verschrieben haben.</p>
        <p>Unsere Vision ist es Waisenkindern ein neues<br>Zuhause zu schaffen wo Sie sicher und behütet<br>aufwachsen können. Wir möchten Kindern, die</p>
      </div>
      <div class="body-text column-right">
        <p>in ihren jungen Jahren schon unglaubliches<br>Leid erleben mussten die Chance auf eine echte<br>Kindheit mit glücklichen Erinnerungen zurück-<br>geben. Am Ende zählt nicht, was Du Dir vorge-<br>nommen hast zu tun, sondern nur das, was Du<br>wirklich tust. Lass uns diese Vision gemeinsam<br>realisieren und wirklich etwas verändern. VEL-<br>TORIS ist Persönlich. Transparent. Authentisch.<br>Einfach anders.</p>
      </div>
      <h2 class="heading heading--donate">So kannst Du spenden</h2>
      <p class="body-text donate-note">Bitte gib bei der Spende an, für welches Projekt du spendest (Waisenhaus/Lebensmittelpaket).<br>Beim Spenden über spendhafen geht die Spende automatisch an das Waisenhaus.</p>
    </div>

    <footer class="donate-band">
      <div class="brand">
        <span class="brand-dot"></span>
        <span class="brand-name">VELTORIS</span>
      </div>
      <span class="divider"></span>
      <div class="donate-options">
        <div class="option">
          <span class="option-mark"></span>
          <span>Paypunkt<br>@veltoris</span>
        </div>
        <div class="option">
          <svg class="option-icon" viewBox="0 0 40 40" aria-hidden="true">
            <rect x="12" y="4" width="22" height="15" rx="2" fill="none" stroke="#fff" stroke-width="2"/>
            <line x1="12" y1="9" x2="34" y2="9" stroke="#fff" stroke-width="2"/>
            <path d="M4 27 h9 l6 -4 h7 a2 2 0 0 1 0 4 h-7 M4 35 h18 l13 -9" fill="none" stroke="#fff" stroke-width="2" stroke-linejoin="round"/>
          </svg>
          <span>Rheinbank Tessel<br>DE47 3150 0721<br>5083 1926 44</span>
        </div>
        <div class="option">
          <span class="option-mark"></span>
          <span>spendhafen.de/<br>4k7q2m</span>
        </div>
      </div>
    </footer>
  </section>
</body>
</html>
```